TRK Website

1. A fully functioning website
2. Should be either Linux, windows or Word Press based
3. Intend to have Velmorix host it
4. Photos should reflect diversity (gender/race)

```html
<!DOCTYPE html>
<html lang="en">
<head>
<meta charset="utf-8">
<title>TRK Management Group</title>
<link href="https://fonts.googleapis.com/css2?family=Poppins:wght@400;500;600;700&family=Open+Sans:wght@400;600&display=swap" rel="stylesheet">
<style>
:root{
  --brand:#3d3b92;
  --brand-dark:#2c2a78;
  --brand-deep:#232166;
  --ink:#222;
  --muted:#8a8a8a;
  --line:#e6e6e6;
  --soft:#f4f4f6;
  --footer:#111;
  --white:#fff;
}
*{box-sizing:border-box;margin:0;padding:0}
html,body{width:1200px;height:3614px;overflow:hidden}
body{font-family:"Open Sans",sans-serif;color:var(--ink);background:var(--white);font-size:11px;line-height:1.6}
h1,h2,h3,h4,.num,.btn,.nav a{font-family:"Poppins",sans-serif}
.wrap{width:727px;margin:0 auto;position:relative}
.btn{display:inline-block;font-size:9px;font-weight:600;letter-spacing:.5px;text-transform:uppercase;padding:9px 20px}
.btn-fill{background:var(--brand);color:#fff}
.btn-line{border:1px solid #fff;color:#fff}
.btn-grey{border:1px solid var(--line);color:var(--ink);background:#fff}
.more{font-family:"Poppins",sans-serif;font-size:8.5px;font-weight:600;color:var(--ink);text-transform:uppercase}

/* top bar */
.topbar{height:24px;background:var(--brand-deep);color:#fff;font-size:9px}
.topbar .wrap{display:flex;justify-content:space-between;align-items:center;height:24px}
.topbar .links{display:flex;gap:14px;align-items:center}

/* header */
.header{height:68px;position:relative;border-bottom:1px solid var(--line)}
.logo{position:absolute;left:34px;top:14px;font-family:"Poppins",sans-serif;font-weight:700;font-size:27px;color:#000}
.nav{position:absolute;left:516px;top:26px;display:flex;gap:26px;align-items:center}
.nav a{font-size:9px;font-weight:500;color:var(--ink);text-decoration:none}

/* hero */
.hero{height:446px;position:relative;background:linear-gradient(100deg,#2d3142 0%,#4a5368 35%,#6f7687 60%,#3a3f52 100%);overflow:hidden}
.hero-copy{position:absolute;left:648px;top:112px;color:#fff;width:360px}
.hero-copy h1{font-size:31px;line-height:1.25;font-weight:700}
.hero-copy p{margin:10px 0 22px;font-size:11px}
.hero-copy .btn{margin-right:26px}
.arrow{position:absolute;top:200px;width:34px;height:34px;border:1px solid rgba(255,255,255,.6);display:flex;align-items:center;justify-content:center}

/* features */
.features{height:242px;background:#fafafa}
.features .wrap{display:flex;gap:12px;padding-top:32px}
.card{flex:1;background:#fff;border:1px solid var(--line);height:170px;padding:26px 14px 0}
.card .head{display:flex;align-items:center;gap:40px;margin-bottom:20px}
.card h3{font-size:12px;font-weight:500;color:var(--brand)}
.card p{font-size:9px;color:var(--muted);line-height:1.6;margin-bottom:10px}

/* services */
.services{height:380px;padding-top:50px}
.sec-head{display:flex;justify-content:space-between;align-items:center;margin-bottom:26px}
.sec-head h2{font-size:19px;font-weight:500}
.mini-arrows{display:flex;gap:8px}
.mini-arrows span{width:22px;height:22px;border-radius:50%;border:1px solid var(--line);display:flex;align-items:center;justify-content:center}
.service-row{display:flex;gap:17px}
.service{flex:1}
.service .pic{height:180px;position:relative}
.service .label{position:absolute;left:0;right:0;bottom:0;background:rgba(0,0,0,.65);color:#fff;text-align:center;font-family:"Poppins",sans-serif;font-weight:600;font-size:12px;padding:4px 0}
.service p{font-size:9px;color:var(--muted);margin-top:8px;line-height:1.6}

/* stats */
.stats{height:302px;background:var(--brand);color:#fff;text-align:center;padding-top:44px}
.stats h2{font-size:15px;font-weight:600;line-height:1.5;width:540px;margin:0 auto 40px}
.stat-row{display:flex;gap:12px}
.stat{flex:1;border:1px solid rgba(255,255,255,.18);height:132px;padding-top:22px}
.stat .num{font-size:30px;font-weight:500;display:block}
.stat h4{font-size:11px;font-weight:500;margin:4px 0}
.stat p{font-size:8.5px;opacity:.8;padding:0 20px;line-height:1.5}

/* projects */
.projects{height:442px;padding-top:38px}
.project{display:flex;height:307px}
.project .pic{width:434px}
.project .info{flex:1;background:var(--soft);text-align:center;padding:80px 34px 0}
.project h3{font-size:14px;font-weight:500}
.project small{font-size:8.5px;color:var(--brand)}
.project p{font-size:9px;color:var(--muted);margin:12px 0 18px}

/* news */
.news{height:509px;background:linear-gradient(var(--soft) 0,var(--soft) 185px,#fff 185px);padding-top:42px;text-align:center}
.news h2{font-size:19px;font-weight:500;margin-bottom:36px}
.news-row{display:flex;gap:17px;text-align:left}
.post{flex:1;border-bottom:1px solid var(--line)}
.post .pic{height:146px}
.post .meta{font-size:8px;color:var(--muted);margin:18px 0 6px}
.post h3{font-size:13px;font-weight:500;line-height:1.35}
.post p{font-size:9px;color:var(--muted);margin:8px 0 18px}
.post .foot{display:flex;justify-content:space-between;padding-bottom:10px;font-size:8.5px;color:var(--muted)}
.dots{display:flex;justify-content:center;gap:6px;margin-top:34px}
.dots i{width:7px;height:7px;border-radius:50%;background:#ccc}
.dots i.on{background:var(--brand)}

/* consultation */
.consult{height:308px;position:relative;background:linear-gradient(90deg,#3d3b92 0%,#4d4ba0 55%,var(--brand-dark) 70%,var(--brand-deep) 100%)}
.consult .wrap{display:flex;gap:20px;padding-top:44px}
.form{width:480px;color:#fff}
.form h2{font-size:19px;font-weight:500;margin-bottom:16px}
.form-grid{display:grid;grid-template-columns:225px 235px;gap:12px 20px}
.field{background:rgba(255,255,255,.14);height:38px;font-size:9px;padding:12px 10px}
.field.tall{grid-row:span 2;height:88px}
.submit{background:#fff;color:var(--brand);text-align:center;font-family:"Poppins",sans-serif;font-weight:600;font-size:9px;padding:12px 0}
.since{width:228px;height:274px;background:#fff;margin-top:-16px;text-align:center;padding:22px 22px 0}
.since h3{font-size:13px;font-weight:600;color:var(--brand);line-height:1.4}
.since .num{font-size:36px;font-weight:600;color:var(--brand-deep);display:block;margin-top:18px}
.since h4{font-size:11px;font-weight:500;color:var(--brand)}
.since p{font-size:9px;color:var(--muted);margin-top:22px}

/* feedback */
.feedback{height:383px;text-align:center;padding-top:48px}
.feedback h2{font-size:19px;font-weight:500;margin-bottom:38px}
.quotes{display:flex;gap:20px;justify-content:center}
.quote{width:232px;font-size:9.5px;color:var(--muted)}
.quote.faded{opacity:.35;padding-top:30px}
.quote .avatar{width:46px;height:46px;border-radius:50%;margin:16px auto 6px;background:linear-gradient(#9aa0ad,#5e6370)}
.quote h4{font-size:11px;color:var(--ink);font-weight:500}
.quote small{font-size:8.5px;color:var(--brand)}

/* partners */
.partners{height:141px;background:var(--soft)}
.partners .wrap{display:flex;justify-content:space-between;align-items:center;height:141px}
.badge{width:92px;height:40px;background:#d2d2d8;border-radius:4px}

/* footer */
.footer{height:369px;background:var(--footer);color:#bbb;position:relative}
.footer .cols{display:flex;padding-top:38px}
.col{width:190px;font-size:9px}
.col h4{color:#fff;font-size:12px;font-weight:500;margin-bottom:20px}
.brand-row{display:flex;align-items:center;gap:8px;margin-bottom:18px}
.brand-row i{width:18px;height:18px;border:2px solid var(--brand);border-radius:3px}
.brand-row span{font-family:"Poppins",sans-serif;color:#fff;font-size:15px;font-weight:600}
.col ul{list-style:none}
.col li{margin-bottom:7px}
.col .news-item{margin-bottom:12px}
.col .news-item b{color:#fff;font-weight:600;display:block}
.footer .btn-grey{background:transparent;color:#fff;border-color:#555;margin-top:16px}
.contact li{display:flex;gap:8px;align-items:center}
.contact .social{display:flex;gap:10px;margin-top:6px}
.contact .social i{width:9px;height:9px;background:#666;border-radius:50%}
.bottom{position:absolute;left:0;right:0;bottom:0;height:56px;border-top:1px solid #222}
.bottom .wrap{display:flex;justify-content:space-between;align-items:center;height:56px;font-size:8.5px}
.bottom nav{display:flex;gap:20px}
</style>
</head>
<body>

<div class="topbar">
  <div class="wrap">
    <span>Orvane Build Your Business Not Just a Website...</span>
    <div class="links"><span>Home</span><span>About Us</span><span>Contact</span><span>&#9993; Free Consultation</span></div>
  </div>
</div>

<header class="header">
  <div class="logo">TRK Management Group</div>
  <nav class="nav">
    <a>+ HOME</a><a>ABOUT US</a><a>SERVICES</a><a>PROJECTS</a><a>BLOG</a><a>SHOP</a><a>CONTACT</a>
    <svg width="10" height="10" viewBox="0 0 10 10"><circle cx="4" cy="4" r="3" fill="none" stroke="#555"/><line x1="6.5" y1="6.5" x2="9.5" y2="9.5" stroke="#555"/></svg>
  </nav>
</header>

<section class="hero" role="img" aria-label="Photo of business people shaking hands in an office">
  <div class="arrow" style="left:8px"><svg width="8" height="10"><path d="M7 1 2 5l5 4" fill="none" stroke="#fff"/></svg></div>
  <div class="arrow" style="right:8px"><svg width="8" height="10"><path d="M1 1l5 4-5 4" fill="none" stroke="#fff"/></svg></div>
  <div class="hero-copy">
    <h1>Get competitive &amp; affordable financial advice.</h1>
    <p>Over 10 years of experience find comprehensive solutions.</p>
    <span class="btn btn-fill">Read more</span><span class="btn btn-line">Meet experts</span>
  </div>
</section>

<section class="features">
  <div class="wrap">
    <div class="card"><div class="head"><svg width="16" height="16"><rect x="1" y="1" width="14" height="14" fill="none" stroke="#bbb"/><path d="M4 11l7-7" stroke="#bbb"/></svg><h3>Professional</h3></div><p>Explain to you how all this mistaken idea of denouncing pleasure and praising pain was born and I will give you a complete.</p><span class="more">Read more</span></div>
    <div class="card"><div class="head"><svg width="16" height="16"><rect x="1" y="1" width="14" height="14" fill="none" stroke="#bbb"/><path d="M4 11l7-7" stroke="#bbb"/></svg><h3>Professional</h3></div><p>Explain to you how all this mistaken idea of denouncing pleasure and praising pain was born and I will give you a complete.</p><span class="more">Read more</span></div>
    <div class="card"><div class="head"><svg width="16" height="16"><rect x="1" y="1" width="14" height="14" fill="none" stroke="#bbb"/><path d="M4 11l7-7" stroke="#bbb"/></svg><h3>Professional</h3></div><p>Explain to you how all this mistaken idea of denouncing pleasure and praising pain was born and I will give you a complete.</p><span class="more">Read more</span></div>
  </div>
</section>

<section class="services">
  <div class="wrap">
    <div class="sec-head"><h2>Our Main Services</h2><div class="mini-arrows"><span><svg width="6" height="8"><path d="M5 1 1 4l4 3" fill="none" stroke="#333"/></svg></span><span><svg width="6" height="8"><path d="M1 1l4 3-4 3" fill="none" stroke="#333"/></svg></span></div></div>
    <div class="service-row">
      <div class="service"><div class="pic" role="img" aria-label="Photo of a desk with a business growth notebook" style="background:linear-gradient(135deg,#6c7a5a,#b9b39a)"><span class="label">Business Growth</span></div><p>Great explorer of the truth, the master builder of human happiness.</p></div>
      <div class="service"><div class="pic" role="img" aria-label="Photo of a consultant presenting to a colleague" style="background:linear-gradient(135deg,#5a4a3e,#a48c74)"><span class="label">Sustainability</span></div><p>Great explorer of the truth, the master builder of human happiness.</p></div>
      <div class="service"><div class="pic" role="img" aria-label="Photo of a team reviewing performance together" style="background:linear-gradient(135deg,#3e3a36,#b08a66)"><span class="label">Performance</span></div><p>Great explorer of the truth, the master builder of human happiness.</p></div>
      <div class="service"><div class="pic" role="img" aria-label="Photo of a smiling businessman in an office" style="background:linear-gradient(135deg,#4a4540,#9c8a78)"><span class="label">Customer Insights</span></div><p>Great explorer of the truth, the master builder of human happiness.</p></div>
    </div>
  </div>
</section>

<section class="stats">
  <div class="wrap">
    <h2>There is some reason behind why people choose Clearpath past 20 years for their business solutions.</h2>
    <div class="stat-row">
      <div class="stat"><span class="num">376</span><h4>Years Of Experience</h4><p>Take a trivial example, which ever undertakes laborious.</p></div>
      <div class="stat"><span class="num">145</span><h4>Best Consultants</h4><p>Explain to you how this mistaken idea denouncing pleasure.</p></div>
      <div class="stat"><span class="num">92</span><h4>Awards Winning</h4><p>Take a trivial example, which ever undertakes laborious.</p></div>
      <div class="stat"><span class="num">289</span><h4>Happy Clients</h4><p>Actual teachings great explorer of the truth master builder.</p></div>
    </div>
  </div>
</section>

<section class="projects">
  <div class="wrap">
    <div class="sec-head"><h2>Latest Projects</h2><span class="btn btn-grey">View all projects</span></div>
    <div class="project">
      <div class="pic" role="img" aria-label="Photo collage of a diverse team working on laptops and meeting" style="background:linear-gradient(135deg,#8a6e58,#d5c2ae 50%,#5e6a7a)"></div>
      <div class="info"><h3>Consumer Products</h3><small>Business Service</small><p>Must explain to you how all this mistaken idea of denouncing pleasure and praising pain was born and we will give you a complete account of the system expound.</p><span class="btn btn-grey">View details</span></div>
    </div>
  </div>
</section>

<section class="news">
  <div class="wrap">
    <h2>Our Latest News</h2>
    <div class="news-row">
      <div class="post"><div class="pic" role="img" aria-label="Photo of hands working on a laptop at a desk" style="background:linear-gradient(135deg,#7f8a94,#dfe3e6)"></div><div class="meta">By admin — January 22, 2018</div><h3>A digital prescription for the pharma industry</h3><p>Pursues or desires to obtain pain of itself but because it is pain, but occasionally can procure great.</p><div class="foot"><span class="more">Read more</span><span>comments</span></div></div>
      <div class="post"><div class="pic" role="img" aria-label="Photo of two colleagues in a meeting room" style="background:linear-gradient(135deg,#4b4f5a,#a9adb6)"></div><div class="meta">By admin — January 22, 2018</div><h3>Why buying a big house is a bad investment</h3><p>To take a trivial example, which of us ever undertakes laborious physical exercise except to obtain some advantage.</p><div class="foot"><span class="more">Read more</span><span>comments</span></div></div>
      <div class="post"><div class="pic" role="img" aria-label="Photo of a team discussing around a table" style="background:linear-gradient(135deg,#5e7a94,#c8d6e2)"></div><div class="meta">By admin — January 22, 2018</div><h3>Successfull business tips in 2017: way to grow</h3><p>Rationally encounter consequences that are extremely painful nor again is there anyone who loves desires.</p><div class="foot"><span class="more">Read more</span><span>comments</span></div></div>
    </div>
    <div class="dots"><i class="on"></i><i></i></div>
  </div>
</section>

<section class="consult" role="img" aria-label="Photo of consultants at work tinted in brand blue">
  <div class="wrap">
    <div class="form">
      <h2>Get a Free Consultation</h2>
      <div class="form-grid">
        <div class="field">Your Name</div>
        <div class="field tall">Special Request (eg: date, time, expert)</div>
        <div class="field">Your Mail</div>
        <div class="field" style="display:flex;justify-content:space-between">Business Growth<svg width="8" height="6"><path d="M1 1l3 3 3-3" fill="none" stroke="#fff"/></svg></div>
        <div class="submit">SUBMIT HERE</div>
      </div>
    </div>
    <div class="since">
      <h3>Since 1991, we provide best service for our clients.</h3>
      <span class="num">26</span><h4>Years of experince</h4>
      <p>About explain to you how all this mistaken idea denouncing pleasure and praising.</p>
    </div>
  </div>
</section>

<section class="feedback">
  <h2>Customer Feedback</h2>
  <div class="quotes">
    <div class="quote faded"><p>"Take a trivial example, which of us ever undertakes laborious physical exercise except to obtain some advantage from it."</p><div style="height:30px"></div><h4>Dana Holt</h4><small>Brightfield</small></div>
    <div class="quote"><p>How all this mistaken idea of denouncing pleasure and praising pain was born and I will give you a complete account.</p><div class="avatar" role="img" aria-label="Customer portrait"></div><h4>Elias Marrow</h4><small>Brightfield</small></div>
    <div class="quote faded"><p>"Take a trivial example, which of us ever undertakes laborious physical exercise except to obtain some advantage from it."</p><div style="height:30px"></div><h4>Dana Holt</h4><small>Brightfield</small></div>
  </div>
  <div class="dots"><i class="on"></i><i></i></div>
</section>

<section class="partners">
  <div class="wrap"><span class="badge"></span><span class="badge"></span><span class="badge"></span><span class="badge"></span><span class="badge"></span><span class="badge"></span></div>
</section>

<footer class="footer">
  <div class="wrap cols">
    <div class="col">
      <div class="brand-row"><i></i><span>Orvane</span></div>
      <p>Over 25 years experience &amp; knowledge international standards, technologicaly changes &amp; industrial systems, we are dedicated to provides the best &amp; solutions to our valued customers.</p>
      <span class="btn btn-grey">Read more</span>
    </div>
    <div class="col"><h4>Usefull Links</h4><ul><li>About Us</li><li>Contact</li><li>Career</li><li>News</li><li>Testimonials</li><li>View All Services</li></ul></div>
    <div class="col"><h4>Latest News</h4>
      <div class="news-item"><b>Successfull business tips in 2017...</b>January 22, 2018</div>
      <div class="news-item"><b>Why buying a big house...</b>January 22, 2018</div>
      <div class="news-item"><b>A digital prescription for the...</b>January 22, 2018</div>
    </div>
    <div class="col contact"><h4>Contact Details</h4><ul>
      <li><svg width="8" height="10"><path d="M4 9C1 5 1 4 1 3.5a3 3 0 0 1 6 0C7 4 7 5 4 9z" fill="none" stroke="#888"/></svg>14 Linden Row, Suite 3, Alderton</li>
      <li><svg width="9" height="9"><path d="M1 1h3l1 2-1.5 1a5 5 0 0 0 2.5 2.5L7 5l2 1v3C4 9 1 5 1 1z" fill="none" stroke="#888"/></svg>+00-555-0142-77</li>
      <li><svg width="10" height="8"><rect x=".5" y=".5" width="9" height="7" fill="none" stroke="#888"/><path d="M.5.5l4.5 4 4.5-4" fill="none" stroke="#888"/></svg>hello@orvane.example</li>
    </ul><div class="social"><i></i><i></i><i></i><i></i><i></i></div></div>
  </div>
  <div class="bottom"><div class="wrap"><span>Copyrights © 2018 All Rights Reserved. Powered by Orvane</span><nav><span>Home</span><span>About Us</span><span>Our Services</span><span>Our Project</span><span>Contact</span></nav></div></div>
</footer>

</body>
</html>
```